Innovative Australian Importation company in Sustainability space needs beautiful website*

We seek your services to provide a clean, modern we rendered logo for or company Red Fern Coastal Supply Pty Ltd, this will be used in all the usual places however you will aso build us our business cards and our website: redferncoastalsupply.example

What we do:
We source innovative products that solve problems in the Aeroponics, Hydroponics, Horticultural, Organics and sustainability space. We source our product from all over the world however our cliant base is predominantly in Australia & New Zealand Region.
Our company's mission is to help retail businesses by providing high-quality products at a competitive price for everyday people to produce healthy sustainable consumables from home, making it easy for the end-user to become more self-sufficient with while remaining environmentally friendly.

Target Market(s)

Aeroponics, Hydroponics, Horticultural, Organics and sustainability space.

Industry/Entity Type

Wholesale

Contact Information for Business Card

We would like these to be very modern and glossy possibly an embosed logo or rounded edges, a little smaller than the traditional?

Logo Text

Red Fern Coastal Supply

Coding

Coded - Design and coding required

Number of Pages Required

1 page

Colors
0355a3

Requirements
Must have
• The websit is bit of a landing page that will provide some minor information on our imported products. and qualify resellers ( Our target Market) from retail clients (the end-user) and provide a private store and check out for our trade customers. (not for Reatil)
Abillity to set up a trade account (must have our approval befor being granted access to shop.)
the abillity to for OEM's and International wholsalers register intrest.
The abillity to register/inquire about our produtc lines for Retailer.
The abillity to provide the end-user a list of resellers.
The ability for promo video
Nice to have
• .
Should not have
• Logo high gloss, 3d rendered

```html
<!DOCTYPE html>
<html lang="en">
<head>
<meta charset="utf-8">
<title>Red Fern Coastal Supply</title>
<link href="https://fonts.googleapis.com/css2?family=Poppins:wght@400;500;600;700;800&family=Roboto:wght@400;500&family=Oswald:wght@500&display=swap" rel="stylesheet">
<style>
:root{
  --brand:#0f7ad3;
  --brand-dark:#0355a3;
  --band:#1a80d6;
  --ink:#111;
  --text:#333;
  --soft:#f4f0ef;
  --footer:#222;
  --white:#fff;
  --leaf:#5f9a2e;
}
*{box-sizing:border-box;margin:0;padding:0}
html,body{width:1200px;height:3333px;overflow:hidden;background:var(--white)}
body{position:relative;font-family:"Roboto",sans-serif;color:var(--text)}
.abs{position:absolute}
.heading{font-family:"Poppins",sans-serif;font-weight:700;color:var(--ink);text-transform:uppercase}
.rule{position:absolute;height:3px;background:var(--brand);width:60px}

/* header */
.brand-name{left:133px;top:22px;font-family:"Poppins",sans-serif;font-weight:700;font-size:25px;line-height:30px;color:var(--brand)}
.brand-dot{left:133px;top:24px;width:0;height:0}
.brand-sub{left:133px;top:56px;font-family:"Poppins",sans-serif;font-weight:700;font-size:17px;color:var(--brand)}
.search{left:599px;top:22px;width:262px;height:33px;border:1px solid #9a9a9a;font-size:10px;padding:10px 14px;color:#333;font-family:"Poppins",sans-serif}
.search svg{position:absolute;right:12px;top:10px}
.register{left:892px;top:22px;width:106px;height:33px;background:var(--brand);color:#fff;font:600 12px/33px "Poppins",sans-serif;text-align:center}
.cart{left:1026px;top:24px}
.cart-count{left:1050px;top:22px;width:17px;height:17px;border-radius:50%;background:var(--brand);color:#fff;font:600 10px/17px "Poppins",sans-serif;text-align:center}
.nav{left:599px;top:73px;display:flex;font:500 14px "Poppins",sans-serif;color:var(--ink)}
.nav span{margin-right:34px}
.nav span:last-child{margin-right:0}
.nav .active{color:var(--brand)}

/* hero */
.hero{left:0;top:106px;width:1200px;height:547px;background:linear-gradient(180deg,#a9b3ad 0%,#7d8d6a 30%,#5f8a2b 55%,#4f7d22 80%,#3d6b1c 100%)}
.hero-title{left:0;top:288px;width:1200px;text-align:center;font:800 34px/42px "Poppins",sans-serif;color:#fff;text-transform:uppercase}
.hero-btn{left:509px;top:405px;width:183px;height:47px;border:3px solid #fff;color:#fff;font:700 15px/41px "Poppins",sans-serif;text-align:center}
.dots{left:548px;top:588px;display:flex;gap:13px;align-items:center}
.dots i{display:block;width:9px;height:9px;border-radius:50%;background:#fff}
.dots i.on{width:14px;height:14px;background:none;border:2px solid #fff}

/* products */
.products-title{left:0;top:694px;width:1200px;text-align:center;font-size:25px}
.card{width:456px;height:320px}
.card .photo{position:absolute;inset:0}
.card .caption{position:absolute;left:14px;bottom:0;width:427px;height:54px;background:#fff;padding:11px 24px}
.card h3{font:600 16px "Poppins",sans-serif;color:var(--ink)}
.card p{font-size:12px;margin-top:3px;color:#222}
.card .shop{position:absolute;right:33px;top:14px;width:81px;height:28px;background:var(--brand);color:#fff;font:600 11px/28px "Poppins",sans-serif;text-align:center}
.card .arrow{position:absolute;right:100px;top:23px}

/* resellers */
.resellers{left:0;top:1517px;width:1200px;height:399px;background:var(--soft)}
.resellers .photo{left:133px;top:42px;width:444px;height:315px;background:linear-gradient(180deg,#8fc347 0%,#6aa835 45%,#dfe6d8 60%,#4d7b8a 100%)}
.resellers h2{left:626px;top:50px;font-size:21px}
.resellers p{left:626px;top:125px;width:435px;font-size:13.6px;line-height:20px;color:#222}
.read-more{left:630px;top:322px;width:98px;height:29px;background:var(--brand);color:#fff;font:600 11px/29px "Poppins",sans-serif;text-align:center}

/* why choose */
.why{left:0;top:1916px;width:1200px;height:489px;background:linear-gradient(180deg,#1c82d8,#1577c9)}
.why h2{left:0;top:40px;width:1200px;text-align:center;color:#fff;font-size:25px}
.why .photo{left:453px;top:131px;width:310px;height:310px;border-radius:50%;background:linear-gradient(160deg,#cfd9d6 0%,#8bb05a 50%,#4d8a27 100%)}
.feature{width:220px;color:#fff}
.feature h4{font:600 14px "Poppins",sans-serif;text-transform:uppercase}
.feature p{font-size:12.4px;line-height:16px;margin-top:6px;color:#e6f1fb}
.feature.left{text-align:right}
.icon{width:57px;height:57px;border-radius:50%;background:#fff;display:flex;align-items:center;justify-content:center}
.link-line{height:1px;background:rgba(255,255,255,.7)}

/* promo */
.promo-title{left:0;top:2440px;width:1200px;text-align:center;font-size:25px}
.video{left:134px;top:2525px;width:934px;height:431px;background:linear-gradient(90deg,#9a948c 0%,#c9c6c2 40%,#e3e3e3 75%,#d5d5d5 100%)}
.video-head{left:589px;top:96px;font:500 31px/37px "Oswald",sans-serif;color:#222;text-transform:uppercase;letter-spacing:-.5px}
.offer{left:591px;top:179px;width:238px;height:113px;background:#eef0f2;padding:12px 24px}
.offer .get{font:700 22px "Poppins",sans-serif;color:var(--brand)}
.offer .big{font:800 60px/60px "Poppins",sans-serif;color:var(--brand);display:flex;align-items:flex-start}
.offer .big small{font-size:25px;line-height:34px;margin-left:4px}
.play{left:440px;top:191px;width:56px;height:56px;border-radius:50%;background:#fff}

/* footer */
.footer{left:0;top:2995px;width:1200px;height:338px;background:var(--footer);color:#fff}
.footer .brand{left:133px;top:90px;font:700 32px/36px "Poppins",sans-serif;color:var(--brand)}
.footer .brand-sub2{left:133px;top:130px;font:600 17px "Poppins",sans-serif;color:var(--brand)}
.col-title{font:600 13px "Poppins",sans-serif;text-transform:uppercase}
.col{font-size:12px;line-height:20px;color:#ddd}
.contact-row{display:flex;align-items:flex-start;gap:12px;font-size:12px;line-height:16px;color:#ddd}
.badge{width:26px;height:26px;border-radius:50%;background:#fff;flex:none;display:flex;align-items:center;justify-content:center}
.divider{left:133px;top:262px;width:934px;height:1px;background:#3a3a3a}
.copy{left:0;top:303px;width:1200px;text-align:center;font-size:10px;color:#ccc}
</style>
</head>
<body>

<header>
  <div class="abs brand-name">RED FERN</div>
  <div class="abs brand-sub">COASTAL SUPPLY</div>
  <div class="abs search">SEARCH
    <svg width="12" height="12" viewBox="0 0 12 12"><circle cx="5" cy="5" r="3.8" fill="none" stroke="#777" stroke-width="1.4"/><path d="M8 8l3 3" stroke="#777" stroke-width="1.4"/></svg>
  </div>
  <div class="abs register">REGISTER</div>
  <svg class="abs cart" width="34" height="32" viewBox="0 0 34 32" aria-label="Cart">
    <path d="M2 4h6l4 17h16l4-12H10" fill="none" stroke="#333" stroke-width="2"/>
    <path d="M12 12h19M13 16h17M16 9v12M21 9v12M26 9v12" stroke="#333" stroke-width="1"/>
    <circle cx="14" cy="27" r="2.5" fill="#333"/><circle cx="26" cy="27" r="2.5" fill="#333"/>
  </svg>
  <div class="abs cart-count">0</div>
  <nav class="abs nav">
    <span class="active">HOME</span><span>ABOUT US</span><span>PRODUCTS</span><span>BLOG</span><span>CONTACT US</span>
  </nav>
</header>

<section>
  <div class="abs hero" role="img" aria-label="Greenhouse with long rows of lettuce under shade netting"></div>
  <h1 class="abs hero-title">Connecting your business<br>to a world of products</h1>
  <div class="abs hero-btn">TRADE ACCOUNT</div>
  <div class="abs dots"><i></i><i></i><i class="on"></i><i></i><i></i></div>
</section>

<section>
  <h2 class="abs heading products-title">Our Products</h2>
  <div class="rule" style="left:570px;top:736px"></div>

  <article class="abs card" style="left:134px;top:780px">
    <div class="photo" role="img" aria-label="Green aeroponic tower trough filled with lettuce" style="background:linear-gradient(180deg,#9ccc5a 0%,#6aa23a 40%,#1d7a5d 70%,#7a6a5e 100%)"></div>
    <div class="caption"><h3>AEROPONICS</h3><p>Lorem Ipsum is simply dummy text of the</p><div class="shop">SHOP NOW</div></div>
  </article>
  <article class="abs card" style="left:609px;top:780px">
    <div class="photo" role="img" aria-label="Hydroponic channels with rows of young plants" style="background:linear-gradient(180deg,#3f7a2c 0%,#5f9a3c 50%,#c8cfc8 80%,#6f8a56 100%)"></div>
    <div class="caption"><h3>HYDROPONICS</h3><p>Lorem Ipsum is simply dummy text of the</p><div class="shop">SHOP NOW</div></div>
  </article>
  <article class="abs card" style="left:134px;top:1128px">
    <div class="photo" role="img" aria-label="Greenhouse interior with hanging baskets and potted plants" style="background:linear-gradient(180deg,#b8bfc0 0%,#6f9a55 40%,#3f7f2a 70%,#2e6a20 100%)"></div>
    <div class="caption"><h3>HORTICULTURAL</h3><p>Lorem Ipsum is simply dummy text of the</p><div class="shop">SHOP NOW</div></div>
  </article>
  <article class="abs card" style="left:609px;top:1128px">
    <div class="photo" role="img" aria-label="Hands holding soil with a small tree growing" style="background:radial-gradient(circle at 70% 35%,#c7e07a 0%,#7fb23f 40%,#3f7a22 100%)"></div>
    <div class="caption"><h3>SUSTAINABILITY SPACE</h3><p>Lorem Ipsum is simply dummy text of the</p>
      <svg class="arrow" width="6" height="10" viewBox="0 0 6 10"><path d="M6 0v10L0 5z" fill="var(--brand)"/></svg>
    </div>
  </article>
</section>

<section class="abs resellers">
  <div class="abs photo" role="img" aria-label="Seedlings growing in foam cubes floating on water"></div>
  <h2 class="abs heading">Qualify Resellers</h2>
  <div class="rule" style="left:626px;top:88px;width:100px"></div>
  <p class="abs">Sed ut perspiciatis unde omnis iste natus error sit voluptatem accusantium doloremque laudantium, totam rem aperiam, eaque ipsa quae ab illo inventore veritatis et quasi architecto beatae vitae dicta sunt explicabo. Nemo enim ipsam voluptatem quia voluptas sit aspernatur aut odit aut fugit, sed quia consequuntur magni dolores eos qui ratione voluptatem sequi nesciunt. Neque porro quisquam est, qui dolorem ipsum quia dolor sit amet, consectetur, adipisci velit, sed quia non numquam eius modi.</p>
  <div class="abs read-more">READ MORE</div>
</section>

<section class="abs why">
  <h2 class="abs heading" style="color:#fff">Why Choose Us</h2>
  <div class="rule" style="left:572px;top:83px;background:#fff"></div>

  <div class="abs link-line" style="left:422px;top:200px;width:70px"></div>
  <div class="abs link-line" style="left:724px;top:200px;width:78px"></div>
  <div class="abs link-line" style="left:422px;top:370px;width:70px"></div>
  <div class="abs link-line" style="left:724px;top:370px;width:78px"></div>

  <div class="abs photo" role="img" aria-label="Greenhouse worker tending rows of lettuce"></div>

  <div class="abs feature left" style="left:128px;top:171px"><h4>Lorem Ipsum</h4><p>Nemo enim ipsam voluptatem quia voluptas sit aspernatur aut odit aut</p></div>
  <div class="abs feature" style="left:875px;top:171px"><h4>Lorem Ipsum</h4><p>Nemo enim ipsam voluptatem quia voluptas sit aspernatur aut odit aut</p></div>
  <div class="abs feature left" style="left:128px;top:340px"><h4>Lorem Ipsum</h4><p>Nemo enim ipsam voluptatem quia voluptas sit aspernatur aut odit aut</p></div>
  <div class="abs feature" style="left:875px;top:340px"><h4>Lorem Ipsum</h4><p>Nemo enim ipsam voluptatem quia voluptas sit aspernatur aut odit aut</p></div>

  <div class="abs icon" style="left:366px;top:172px">
    <svg width="30" height="28" viewBox="0 0 30 28"><rect x="12" y="1" width="16" height="10" rx="2" fill="none" stroke="var(--brand)" stroke-width="2"/><circle cx="9" cy="13" r="4" fill="var(--brand)"/><path d="M1 27c0-6 4-9 8-9s8 3 8 9z" fill="var(--brand)"/></svg>
  </div>
  <div class="abs icon" style="left:801px;top:172px">
    <svg width="28" height="24" viewBox="0 0 28 24"><rect x="1" y="6" width="26" height="17" rx="2" fill="var(--brand)"/><path d="M10 6V2h8v4" fill="none" stroke="var(--brand)" stroke-width="2"/><rect x="12" y="12" width="4" height="4" fill="#fff"/></svg>
  </div>
  <div class="abs icon" style="left:366px;top:341px">
    <svg width="30" height="30" viewBox="0 0 30 30"><circle cx="15" cy="15" r="10" fill="none" stroke="var(--brand)" stroke-width="4" stroke-dasharray="5 3"/><circle cx="15" cy="15" r="4" fill="var(--brand)"/></svg>
  </div>
  <div class="abs icon" style="left:801px;top:341px">
    <svg width="28" height="30" viewBox="0 0 28 30"><circle cx="14" cy="12" r="3" fill="var(--brand)"/><path d="M14 16v13M14 20l-7-6M14 20l7-6M5 6l3 3M23 6l-3 3M14 2v5" stroke="var(--brand)" stroke-width="2.4" fill="none"/></svg>
  </div>
</section>

<section>
  <h2 class="abs heading promo-title">Promo Video</h2>
  <div class="rule" style="left:572px;top:2485px"></div>
  <div class="abs video">
    <div class="abs" role="img" aria-label="Seedling sprouting from clay pebbles in a glass pot" style="left:0;top:0;width:520px;height:431px;background:radial-gradient(ellipse at 55% 45%,#5fae2c 0%,#6f8a4a 30%,rgba(140,110,100,.6) 60%,transparent 85%)"></div>
    <div class="abs play">
      <svg width="56" height="56" viewBox="0 0 56 56"><circle cx="28" cy="28" r="21" fill="none" stroke="#222" stroke-width="3"/><path d="M23 18v20l15-10z" fill="#222"/></svg>
    </div>
    <div class="abs video-head">Lorem ipsum dolor<br>sit amet consectetur</div>
    <div class="abs offer">
      <div class="get">GET</div>
      <div class="big">50%<small>OFF</small></div>
    </div>
  </div>
</section>

<footer class="abs footer">
  <div class="abs brand">RED FERN</div>
  <div class="abs brand-sub2">COASTAL SUPPLY</div>

  <div class="abs col-title" style="left:495px;top:46px">Menu</div>
  <div class="abs col" style="left:495px;top:80px">HOME<br>ABOUT US<br>PRODUCTS<br>BLOG<br>CONTACT US</div>

  <div class="abs col-title" style="left:686px;top:46px">Contact Us</div>
  <div class="abs contact-row" style="left:684px;top:84px">
    <div class="badge"><svg width="10" height="14" viewBox="0 0 10 14"><path d="M5 0a5 5 0 0 1 5 5c0 4-5 9-5 9S0 9 0 5a5 5 0 0 1 5-5z" fill="#222"/><circle cx="5" cy="5" r="1.8" fill="#fff"/></svg></div>
    <div>27 Tidewater Lane<br>Port Kessing, NSW 2491</div>
  </div>
  <div class="abs contact-row" style="left:684px;top:136px">
    <div class="badge"><svg width="12" height="12" viewBox="0 0 12 12"><path d="M2 0l3 3-1.5 1.5a7 7 0 0 0 4 4L9 7l3 3-2 2C5 12 0 7 0 2z" fill="#222"/></svg></div>
    <div>Call Us<br>02 5550 1742</div>
  </div>
  <div class="abs contact-row" style="left:684px;top:186px">
    <div class="badge"><svg width="12" height="9" viewBox="0 0 12 9"><rect width="12" height="9" fill="#222"/><path d="M0 0l6 5 6-5" stroke="#fff" fill="none"/></svg></div>
    <div>E mail Us<br>info@redferncoastalsupply.example</div>
  </div>

  <div class="abs col-title" style="left:967px;top:46px">Follow Us</div>
  <div class="abs contact-row" style="left:965px;top:84px"><div class="badge"></div><div>Like us on<br>LEAFBOOK</div></div>
  <div class="abs contact-row" style="left:965px;top:134px"><div class="badge"></div><div>Follow us on<br>CHIRPER</div></div>
  <div class="abs contact-row" style="left:965px;top:185px"><div class="badge"></div><div>Follow us on<br>WORKLINK</div></div>

  <div class="abs divider"></div>
  <div class="abs copy">Copyright © 2020 All Rights Reserved</div>
</footer>

</body>
</html>
```